Velmo BUSINESS CARD

Design an attention-grabbing business cards. Draw inspiration from the provided logo file. Please use the same font style as in the logo.
the back side of the card is for accent/decoration.

Contact Information for Business Card

PLEASE USE PROVIDED BUSINESS CARD SAMPLE

Other font styles liked:
• LUMETTE

Colors
EB3D1F
EC4F4E
F09395
F8D3D4
FCEDEE

Requirements
Must have
• RED, BLACK COLORS, SOLID BACK COLOR
Nice to have
• MAKE IT FANCY

```html
<!DOCTYPE html>
<html lang="en">
<head>
<meta charset="utf-8">
<title>Velmo Business Card</title>
<link href="https://fonts.googleapis.com/css2?family=Lato:wght@400;700;900&display=swap" rel="stylesheet">
<style>
  :root {
    --red: #e02231;
    --black: #1f1b1c;
    --white: #ffffff;
    --bg: #d9d9d6;
  }
  * { margin: 0; padding: 0; box-sizing: border-box; }
  html, body { width: 1200px; height: 801px; overflow: hidden; }
  body {
    background: var(--bg);
    font-family: "Lato", sans-serif;
    position: relative;
  }
  .card {
    position: absolute;
    top: 245px;
    width: 540px;
    height: 310px;
    background: var(--white);
    border: 2px solid var(--red);
    border-radius: 16px;
    overflow: hidden;
  }
  .card--front { left: 40px; }
  .card--back { left: 620px; }

  .brand { position: absolute; display: flex; align-items: center; }
  .brand__square { background: var(--black); flex: none; }
  .brand__name {
    font-family: "Lato", sans-serif;
    font-weight: 700;
    color: var(--black);
    line-height: 1;
  }

  /* front */
  .card--front .brand { left: 26px; top: 28px; gap: 12px; }
  .card--front .brand__square { width: 44px; height: 44px; }
  .card--front .brand__name { font-size: 38px; }

  .name-tab {
    position: absolute; left: 0; top: 104px;
    width: 16px; height: 44px; background: var(--red);
  }
  .person { position: absolute; left: 34px; top: 100px; }
  .person__name {
    font-family: "Lato", sans-serif;
    font-weight: 900;
    color: var(--red);
    font-size: 23px;
    letter-spacing: 0.04em;
    text-transform: uppercase;
    line-height: 1.1;
  }
  .person__title { font-size: 13px; color: var(--black); margin-top: 2px; }

  .contacts { position: absolute; left: 50px; top: 168px; list-style: none; }
  .contacts li {
    display: flex; align-items: center; gap: 7px;
    font-size: 13px; color: var(--black); line-height: 19px;
  }
  .contacts svg { width: 11px; height: 11px; flex: none; }
  .address {
    position: absolute; left: 68px; top: 252px;
    font-size: 13px; color: var(--black); line-height: 18px; font-style: normal;
  }
  .feature-block {
    position: absolute; right: 34px; top: 52px;
    width: 190px; height: 190px; background: var(--black);
  }

  /* back */
  .card--back .brand { left: 50%; top: 50%; transform: translate(-50%, -50%); gap: 18px; }
  .card--back .brand__square { width: 88px; height: 88px; }
  .card--back .brand__name { font-size: 76px; }
</style>
</head>
<body>
  <section class="card card--front" aria-label="Front of card">
    <div class="brand">
      <div class="brand__square"></div>
      <span class="brand__name">Velmo</span>
    </div>

    <div class="name-tab"></div>
    <div class="person">
      <h1 class="person__name">Alan Reyes</h1>
      <p class="person__title">President</p>
    </div>

    <ul class="contacts">
      <li>
        <svg viewBox="0 0 12 12"><path fill="var(--red)" d="M1 3.5C1 2 2.5 1 6 1s5 1 5 2.5v1H8.5v-1h-5v1H1zM2.5 5.5h7L11 10.5H1z"/></svg>
        555-014-2290
      </li>
      <li>
        <svg viewBox="0 0 12 12"><rect x="3" y="0.8" width="6" height="10.4" rx="1" fill="none" stroke="var(--red)" stroke-width="1.2"/><circle cx="6" cy="9.3" r="0.6" fill="var(--red)"/></svg>
        555-014-7731
      </li>
      <li>
        <svg viewBox="0 0 12 12"><rect x="0.5" y="2" width="11" height="8" fill="var(--red)"/><path d="M0.8 2.4L6 6.6l5.2-4.2" fill="none" stroke="var(--white)" stroke-width="1"/></svg>
        AReyes@velmo-llc.com
      </li>
      <li>
        <svg viewBox="0 0 12 12"><circle cx="6" cy="6" r="5.3" fill="var(--red)"/><path d="M0.8 6h10.4M6 0.8c-2.2 2.8-2.2 7.6 0 10.4M6 0.8c2.2 2.8 2.2 7.6 0 10.4" fill="none" stroke="var(--white)" stroke-width="0.7"/></svg>
        WWW.Velmo-LLC.Com
      </li>
    </ul>

    <address class="address">
      418 Harlow Lane,<br>
      Brookfield, OH, 40215
    </address>

    <div class="feature-block"></div>
  </section>

  <section class="card card--back" aria-label="Back of card">
    <div class="brand">
      <div class="brand__square"></div>
      <span class="brand__name">Velmo</span>
    </div>
  </section>
</body>
</html>
```